SEO and image area for top of invitation website

We need to add an area on our final category pages for SEO text. Instead of just adding text, we'd like to develop a graphical approach that keeps with our soft, feminine look.

You can view an example of our current final category page at http://www.partywren.example/invitations/boy-birthday

I've attached an image of what we're thinking it could look like, but you're welcome to alter the design.

The area should be the same width as our site, but can be any height you determine appropriate.

The winner of this project may be approached to develop the additional designs and backgrounds for us as another project. We additionally have several other projects we're interested in doing with the winner.

We have had a question about the right side of the banner, and what "Free Unlimited Proofs" mean.

About Free Unlimited Proofs:

We are a custom invitation printing company. When a customer orders an invitation from us, they tell us what information we want on the invitation. We then create an electronic sample, or "proof", of what it will look like. We then email it to the customer and they can tell us if they want to make any more changes. We will continue to send them samples, or what we call "proofs", until they are completely satisfied with the way it looks.

We offer Free UNLIMITED Proofs. Compared to our competitors, we are the only one to offer free unlimited proofs.

So, for the right side of this banner, we need an image, or a badge, promoting that we offer free unlimited proofs, and you can include that we are the only ones to do it, if your design has space for that information.

Also, keep in mind, that for other category pages, we may create different images or badges to put in this area - such as for our Low Price Guarantee or to promote a coupon or specific product, for example. So, your design should be able to work with various images on the right side.

Target Market(s)

Our demographic is 100% women, ages 25-60.

Industry/Entity Type

Seo

Requirements
Must have
• The area must have 3 things:
1) Area for the title of the page.
2) Area for SEO text describing the category page.
3) Area for an image. Keep in mind that this image may change for each category page. For this project, you will create an image for our offering of "Free Unlimited Proofs". On other pages, we may display other images we create such as "Low Price Guarantee" or images of certain products we'd like to promote. Just keep this in mind when you're making the design flow.
Nice to have
• Optional: Light design background. We wouldn't mind there being a slight graphical background to this area, to keep it interesting to the eye. Then, for other category pages, we may make additional backgrounds to use in this box area.

```html
<!DOCTYPE html>
<html lang="en">
<head>
<meta charset="utf-8">
<title>Boy Birthday Invitations – Party Wren</title>
<link rel="stylesheet" href="https://fonts.googleapis.com/css2?family=Bitter:wght@400&family=Noto+Serif:ital,wght@0,400;0,700;1,700&family=Open+Sans:wght@400;600;700&display=swap">
<style>
  :root{
    --ink:#5a5050;
    --mauve:#7d6769;
    --title-gold:#f6d74c;
    --teal:#3fb7a3;
    --teal-dark:#2e9e8b;
    --link:#27a394;
    --panel:#efedec;
    --rule:#d9d6d5;
    --topbar:#f2f2f2;
    --card-border:#d3d0cf;
    --btn:#f7d04e;
    --btn-edge:#e0b62f;
  }
  *{box-sizing:border-box;margin:0;padding:0}
  html,body{width:1200px;height:960px;overflow:hidden;background:#fff;color:var(--ink);font-family:"Open Sans",sans-serif}
  .page{position:relative;width:1200px;height:960px}

  .topbar{position:absolute;left:0;top:0;width:1200px;height:28px;background:var(--topbar);border-bottom:1px solid var(--rule);display:flex;justify-content:center;align-items:center;font-size:12.5px;font-weight:600;color:#555}
  .topbar span{padding:0 12px;border-right:1px solid var(--rule);line-height:28px;display:flex;align-items:center;gap:7px}
  .topbar span:last-child{border-right:0}
  .topbar svg{fill:#555}

  .logo{position:absolute;left:147px;top:44px;display:flex;align-items:center;gap:14px}
  .logo-mark{width:58px;height:58px;background:var(--mauve);border-radius:4px}
  .logo-name{font-family:"Bitter",serif;font-size:37px;color:#6b5c5e}

  .search{position:absolute;left:486px;top:64px;width:276px;height:45px;border:1px solid #e5e3e2;border-radius:4px;background:#fafafa}
  .search b{position:absolute;right:6px;top:7px;width:62px;height:28px;background:#c9c6c5;color:#fff;font-family:"Noto Serif",serif;font-size:12px;line-height:28px;text-align:center;border-radius:3px}
  .account{position:absolute;left:783px;top:76px;font-family:"Noto Serif",serif;font-size:12px;color:#555;display:flex;gap:16px;align-items:center}

  .nav{position:absolute;left:144px;top:135px;width:914px;height:46px;border-top:1px solid var(--rule);border-bottom:1px solid var(--rule);display:flex;align-items:center;gap:38px;padding-left:19px;font-family:"Bitter",serif;font-size:18.5px;color:#6b6163}

  .crumbs{position:absolute;left:144px;top:199px;font-family:"Noto Serif",serif;font-size:11.5px;color:#555}
  .crumbs a{color:var(--link);text-decoration:none}

  .seo{position:absolute;left:140px;top:239px;width:666px;height:186px;background:var(--panel)}
  .seo-title{height:41px;background:var(--mauve);color:var(--title-gold);font-family:"Bitter",serif;font-size:26px;line-height:41px;padding-left:20px}
  .seo-text{position:absolute;left:20px;top:58px;width:520px;font-family:"Noto Serif",serif;font-size:12.8px;line-height:21px;color:#6a6264}
  .seo-text b{color:#4f4749}
  .seo-art{position:absolute;left:555px;top:24px;width:100px;height:152px;border-radius:40px 40px 8px 8px;background:linear-gradient(180deg,#f8d43d 0%,#f3c63a 50%,#e9e7e6 51%,#f4f3f2 100%)}

  .proofs{position:absolute;left:822px;top:239px;width:248px;height:186px;background:var(--panel)}
  .proofs-band{position:relative;height:44px;background:var(--teal);color:#fff;font-family:"Bitter",serif;font-size:21px;line-height:42px;text-align:center;border-radius:4px 4px 0 0}
  .proofs-band:after{content:"";position:absolute;left:0;top:44px;border-left:124px solid transparent;border-right:124px solid transparent;border-top:11px solid var(--teal-dark)}
  .proofs-text{position:absolute;left:15px;top:68px;width:115px;font-family:"Noto Serif",serif;font-size:13px;line-height:19px;color:#6a6264}
  .proofs-text b{color:#4f4749}
  .proofs-only{position:absolute;left:15px;top:136px;font-family:"Noto Serif",serif;font-style:italic;font-weight:700;font-size:12px;line-height:19px;color:var(--link)}
  .proofs-art{position:absolute;left:165px;top:78px;width:80px;height:104px;border-radius:40px 40px 20px 20px;background:radial-gradient(circle at 40% 30%,#bde6de 0%,#f3f2f1 70%)}

  .sort{position:absolute;left:158px;top:435px;font-family:"Noto Serif",serif;font-size:12px;color:#555;display:flex;align-items:baseline;gap:19px}
  .sort strong{font-weight:400;font-size:15px}
  .pager{position:absolute;left:852px;top:435px;display:flex;align-items:center;gap:8px;font-family:"Open Sans",sans-serif;font-size:12.5px;color:var(--link)}
  .pager i{width:20px;height:20px;border-radius:50%;display:block;position:relative}
  .pager .prev{background:#cfcccb}
  .pager .next{background:var(--teal)}
  .pager i:after{content:"";position:absolute;top:6px;width:0;height:0;border-top:4px solid transparent;border-bottom:4px solid transparent}
  .pager .prev:after{left:6px;border-right:7px solid #fff}
  .pager .next:after{left:8px;border-left:7px solid #fff}

  .filters{position:absolute;left:144px;top:490px;width:228px}
  .filter-head{font-family:"Bitter",serif;font-size:16px;color:#6b6163;padding-left:9px;position:relative;height:26px}
  .filter-head:before{content:"";position:absolute;left:9px;top:6px;border-top:5px solid transparent;border-bottom:5px solid transparent;border-left:6px solid #777}
  .filter-head span{padding-left:16px}
  .colors{list-style:none;padding:8px 0 0 26px;font-size:12px;line-height:19px;color:#666}
  .colors li{display:flex;align-items:center;gap:8px}
  .colors i{width:14px;height:14px;border-radius:50%;display:inline-block;border:1px solid rgba(0,0,0,.15)}
  .colors .all{padding-left:3px;text-transform:uppercase}
  .filter-block{border-top:3px solid var(--rule);margin-top:9px;padding-top:13px;height:60px}

  .card{position:absolute;width:212px;height:211px;border:1px solid var(--card-border);background:#f4f3f3}
  .card .art{position:absolute;left:50%;transform:translateX(-50%);top:0}
  .quick{position:absolute;left:50%;bottom:-10px;transform:translateX(-50%);width:92px;height:24px;background:var(--btn);border:1px solid var(--btn-edge);border-radius:5px;font-size:11.5px;font-weight:700;color:#5a4a2a;text-align:center;line-height:22px}
</style>
</head>
<body>
<div class="page">

  <div class="topbar">
    <span><svg width="16" height="12" viewBox="0 0 16 12"><rect x="0" y="1" width="10" height="7"/><path d="M10 3h3l3 3v2h-6z"/><circle cx="3" cy="10" r="1.8"/><circle cx="12" cy="10" r="1.8"/></svg>FREE SHIPPING on orders over $150 – no coupon needed!</span>
    <span><svg width="16" height="13" viewBox="0 0 16 13"><path d="M1 1h9v6H4l-3 3z"/><path d="M11 4h4v6l-2-2h-5V8h3z"/></svg>Live Help</span>
    <span><svg width="16" height="13" viewBox="0 0 16 13"><path d="M1 4c0-3 14-3 14 0v2h-4V4H5v2H1z"/><rect x="3" y="7" width="10" height="5" rx="1"/></svg>555.014.2290</span>
    <span><svg width="14" height="14" viewBox="0 0 14 14"><path d="M1 1h6l6 6-6 6-6-6z"/></svg>Become a Designer · Earn Commission</span>
  </div>

  <div class="logo">
    <div class="logo-mark"></div>
    <div class="logo-name">Party Wren</div>
  </div>

  <div class="search"><b>search</b></div>
  <div class="account">
    <span>LOGIN</span><span>CREATE ACCOUNT</span>
    <span style="display:flex;align-items:center;gap:10px"><svg width="18" height="16" viewBox="0 0 18 16" fill="#666"><path d="M0 1h3l3 9h9l2-6H5" fill="none" stroke="#666" stroke-width="1.8"/><circle cx="7" cy="14" r="1.6"/><circle cx="14" cy="14" r="1.6"/></svg><span style="font-size:16px">0</span></span>
  </div>

  <nav class="nav">
    <span>Wedding</span><span>Party</span><span>Baby and Kids</span><span>Holiday</span><span>Graduation</span><span>Business</span><span>Stationery</span>
  </nav>

  <div class="crumbs"><a href="#">Party</a> · <a href="#">Kids Birthday Party Invitations</a> · Boy Birthday Invitations</div>

  <section class="seo">
    <h1 class="seo-title" style="font-weight:400">Boy Birthday Invitations</h1>
    <p class="seo-text"><b>PartyWren.com</b> offers the easiest, most intuitive invitation customizer on the market. With just a few simple clicks, you'll have the invitation perfect for your special occassion or event. While many of our competitors offers just a few simple font colors, most of our invitations have a large color palette and font selection to choose from, with no restriction of how many you can use on one invitation.</p>
    <div class="seo-art" role="img" aria-label="Illustration of a yellow bird perched on an open envelope"></div>
  </section>

  <aside class="proofs">
    <div class="proofs-band">Free Unlimited Proofs</div>
    <p class="proofs-text">Your order will be <b>PERFECT</b>, every time</p>
    <p class="proofs-only">Only at<br>PartyWren.com</p>
    <div class="proofs-art" role="img" aria-label="Line illustration of a hand tapping a circular refresh arrow"></div>
  </aside>

  <div class="sort"><strong>Sort By:</strong><span>Price</span><span>Name</span><span>Vendor</span></div>
  <div class="pager"><i class="prev"></i><span>1</span><span>2</span><span>3</span><span>4</span><span>5</span><span>6</span><span>7</span><span>8</span><span>9</span><i class="next"></i></div>

  <div class="filters">
    <div class="filter-head"><span>Filter By Color</span></div>
    <ul class="colors">
      <li><i style="background:#333"></i>Black</li>
      <li><i style="background:#5b8fe8"></i>Blue</li>
      <li><i style="background:#8a5a44"></i>Brown</li>
      <li><i style="background:#f2b418"></i>Gold</li>
      <li><i style="background:#7ad67a"></i>Green</li>
      <li><i style="background:#cfcfcf"></i>Grey</li>
      <li><i style="background:#f6f3dc"></i>Ivory</li>
      <li><i style="background:#f6a55c"></i>Orange</li>
      <li><i style="background:#f7c2ea"></i>Pink</li>
      <li><i style="background:#7c2170"></i>Purple</li>
      <li><i style="background:#e0524c"></i>Red</li>
      <li><i style="background:#f1f4f6"></i>Silver</li>
      <li><i style="background:#fff"></i>White</li>
      <li><i style="background:#f7ea6a"></i>Yellow</li>
      <li class="all">All colors</li>
    </ul>
    <div class="filter-block"><div class="filter-head"><span>Filter By Card Size</span></div></div>
    <div class="filter-block"><div class="filter-head"><span>Filter By # of Photos</span></div></div>
    <div class="filter-block"><div class="filter-head"><span>Filter By Designer</span></div></div>
  </div>

  <div class="card" style="left:391px;top:485px"><div class="art" role="img" aria-label="Pirate party invitation with parrot, pirate ship and child photo" style="width:152px;height:210px;background:linear-gradient(135deg,#3aa8e0 0%,#d9322b 35%,#f39a1e 60%,#8cc63f 100%)"></div><div class="quick">Quick View</div></div>
  <div class="card" style="left:619px;top:485px"><div class="art" role="img" aria-label="Star-patterned birthday invitation with child photo and blue name band" style="width:152px;height:210px;background:linear-gradient(180deg,#8cc63f 0%,#6a8f4a 25%,#29a8e0 55%,#f39a1e 75%,#8cc63f 100%)"></div><div class="quick">Quick View</div></div>
  <div class="card" style="left:846px;top:485px"><div class="art" role="img" aria-label="Orange dinosaur shaped birthday invitation" style="width:210px;height:130px;background:radial-gradient(ellipse at 55% 55%,#f7a81e 0%,#f39a1e 55%,#fff 72%)"></div><div class="quick">Quick View</div></div>
  <div class="card" style="left:391px;top:715px"><div class="art" role="img" aria-label="Bowling party invitation with bowling ball and pins" style="width:76px;height:210px;background:linear-gradient(180deg,#d9322b 0%,#3aa8e0 20%,#6cc3ea 100%)"></div><div class="quick">Quick View</div></div>
  <div class="card" style="left:619px;top:715px"><div class="art" role="img" aria-label="Water slide party invitation with boy sliding" style="width:206px;height:130px;background:linear-gradient(160deg,#8cc63f 0%,#8cc63f 40%,#f5d94a 55%,#e94b2b 70%,#8cc63f 100%)"></div><div class="quick">Quick View</div></div>
  <div class="card" style="left:846px;top:715px"><div class="art" role="img" aria-label="Space party invitation with green alien in flying saucer" style="width:210px;height:130px;background:linear-gradient(135deg,#29a8e0 0%,#1f8fcf 100%)"></div><div class="quick">Quick View</div></div>
  <div class="card" style="left:391px;top:945px"><div class="art" role="img" aria-label="Yellow party invitation" style="width:158px;height:20px;background:#f3d52a"></div></div>
  <div class="card" style="left:619px;top:945px"><div class="art" role="img" aria-label="Cream party invitation" style="width:158px;height:20px;background:#f8e4a8"></div></div>
  <div class="card" style="left:846px;top:945px"><div class="art" role="img" aria-label="Green and orange party invitation" style="width:210px;height:20px;background:linear-gradient(90deg,#f39a1e,#8cc63f)"></div></div>

</div>
</body>
</html>
```